Simple Business Card Design

Professional/clean business card with custom logo included in layout.

Target Market(s)

N/A

Industry/Entity Type

Business

Contact Information for Business Card

Name: Marlene Voskin, PT; NV Medicaid Provider; Phone: (775) 918-2246; Toll-free phone: (877) 461-5092; email: mar@tidewellbranchsystemsltd.example

Font styles to use
Serif
Decorative
Script

Requirements
Must have
• See "details" above.
Nice to have
• Would be interested to see dark vs. light/grayscale backgrounds that accentuate/contrast the logo colors. (I.e. dark navy background w/ white or grey text, etc.)

```html
<!DOCTYPE html>
<html lang="en">
<head>
<meta charset="utf-8">
<title>Tidewell Branch Systems, Ltd. – Business Card</title>
<link rel="stylesheet" href="https://fonts.googleapis.com/css2?family=Cinzel:wght@400;600&family=Cormorant+Garamond:wght@500;600&display=swap">
<style>
  :root {
    --navy: #141a3f;
    --paper: #ffffff;
    --slate: #7b7b7b;
    --ink: #2a2d3e;
    --soft-white: #eeeeee;
    --stage: #e6e6e3;
  }
  * { margin: 0; padding: 0; box-sizing: border-box; }
  html, body { width: 1200px; height: 948px; overflow: hidden; background: var(--stage); }
  .canvas {
    position: relative; width: 1200px; height: 948px;
    display: flex; align-items: center; justify-content: center; gap: 40px;
  }
  .card {
    position: relative; width: 540px; height: 309px; overflow: hidden;
    box-shadow: 0 6px 18px rgba(0,0,0,.18);
  }
  /* Front */
  .card-front { background: var(--paper); color: var(--ink); }
  .card-front .band {
    position: absolute; left: 0; bottom: 0; width: 100%; height: 96px;
  }
  .brand {
    position: absolute; display: flex; align-items: center; gap: 12px;
  }
  .brand-mark {
    flex: none; border-radius: 50%; background: var(--navy);
  }
  .brand-name {
    font-family: "Cinzel", serif; font-weight: 600; letter-spacing: .08em; line-height: 1.15;
  }
  .card-front .brand { left: 40px; top: 30px; }
  .card-front .brand-mark { width: 44px; height: 44px; }
  .card-front .brand-name { font-size: 17px; color: var(--navy); }
  .holder {
    position: absolute; left: 40px; top: 104px;
    font-family: "Cinzel", serif; font-size: 19px; font-weight: 600; color: var(--navy); letter-spacing: .03em;
  }
  .holder .title { font-size: 12px; font-weight: 400; letter-spacing: .06em; }
  .contact-list {
    list-style: none; position: absolute; font-family: "Cormorant Garamond", serif; font-weight: 600; font-size: 15px;
  }
  .contact-list li { display: flex; align-items: center; gap: 10px; height: 28px; }
  .contact-list svg { width: 20px; height: 20px; flex: none; }
  .contact-main { left: 40px; top: 140px; color: var(--ink); }
  .contact-band { left: 40px; top: 228px; color: var(--soft-white); }
  /* Back */
  .card-back { background: var(--slate); color: var(--soft-white); }
  .card-back .brand { left: 50%; top: 96px; transform: translateX(-50%); }
  .card-back .brand-mark { width: 62px; height: 62px; background: var(--navy); border: 3px solid var(--soft-white); }
  .card-back .brand-name { font-size: 22px; color: var(--soft-white); }
  .web {
    position: absolute; left: 0; right: 0; top: 212px; text-align: center;
    font-family: "Cormorant Garamond", serif; font-weight: 600; font-size: 15px; letter-spacing: .04em;
  }
</style>
</head>
<body>
<main class="canvas">
  <section class="card card-front" aria-label="Business card front">
    <svg class="band" viewBox="0 0 540 96" preserveAspectRatio="none" aria-hidden="true">
      <polygon points="0,14 300,14 340,0 540,0 540,96 0,96" fill="var(--navy)"/>
    </svg>
    <div class="brand">
      <span class="brand-mark" aria-hidden="true"></span>
      <span class="brand-name">TIDEWELL BRANCH<br>SYSTEMS, LTD.</span>
    </div>
    <p class="holder">MARLENE VOSKIN, PT<span class="title">; NV MEDICAID PROVIDER</span></p>
    <ul class="contact-list contact-main">
      <li>
        <svg viewBox="0 0 20 20" aria-hidden="true"><circle cx="10" cy="10" r="10" fill="var(--navy)"/><path d="M7 5.5l2 2-1 1.2c.6 1.3 1.5 2.2 2.8 2.8l1.2-1 2 2-1.3 1.5C9.6 13.6 6.4 10.4 5.5 7z" fill="#fff"/></svg>
        (775) 918-2246
      </li>
      <li>
        <svg viewBox="0 0 20 20" aria-hidden="true"><circle cx="10" cy="10" r="10" fill="var(--navy)"/><rect x="5" y="6.5" width="10" height="7" fill="none" stroke="#fff" stroke-width="1.2"/><path d="M5 6.5l5 4 5-4" fill="none" stroke="#fff" stroke-width="1.2"/></svg>
        mar@tidewellbranchsystemsltd.example
      </li>
    </ul>
    <ul class="contact-list contact-band">
      <li>
        <svg viewBox="0 0 20 20" aria-hidden="true"><circle cx="10" cy="10" r="10" fill="#fff"/><path d="M7 5.5l2 2-1 1.2c.6 1.3 1.5 2.2 2.8 2.8l1.2-1 2 2-1.3 1.5C9.6 13.6 6.4 10.4 5.5 7z" fill="var(--navy)"/></svg>
        (877) 461-5092 (TF)
      </li>
      <li>
        <svg viewBox="0 0 20 20" aria-hidden="true"><circle cx="10" cy="10" r="10" fill="#fff"/><path d="M10 4.5a3.5 3.5 0 0 1 3.5 3.5c0 2.6-3.5 7-3.5 7s-3.5-4.4-3.5-7A3.5 3.5 0 0 1 10 4.5z" fill="var(--navy)"/><circle cx="10" cy="8" r="1.3" fill="#fff"/></svg>
        Street Name, City Name, Zip Code 00000
      </li>
    </ul>
  </section>

  <section class="card card-back" aria-label="Business card back">
    <div class="brand">
      <span class="brand-mark" aria-hidden="true"></span>
      <span class="brand-name">TIDEWELL BRANCH<br>SYSTEMS, LTD.</span>
    </div>
    <p class="web">www.tidewellbranchsystemsltd.example</p>
  </section>
</main>
</body>
</html>
```